Calloway Holdings Website Design

We are a private equity firm based with offices based in Hong Kong, Singapore, London and Paris. Our focus is investments in property development projects, corporate ventures and loans.

We require the development of a new website and you will have to select relevant images from the likes of PixelVaultPics or other stock photo libraries.

We will need a design done for a PC based website and the designer selected with the favored design will also need to produce some concepts for a responsive website.

Target Market(s)

Sophisticated investors looking to invest in high return property development, businesses and mortgages.

Industry/Entity Type

Investment

Number of Pages Required

5+ page

Font styles to use
Serif
Sans Serif

Colors
0255a3
00a990

Requirements
Must have
• Clean modern feel and must portray stability and professionalism.

```html
<!DOCTYPE html>
<html lang="en">
<head>
<meta charset="utf-8">
<title>Calloway Holdings</title>
<link href="https://fonts.googleapis.com/css2?family=Magra:wght@400;700&family=Montserrat:wght@400;700&family=Arimo:wght@400;700&display=swap" rel="stylesheet">
<style>
:root{
  --blue:#0255a3;
  --blue-bright:#0565c8;
  --teal:#00a990;
  --ink:#222;
  --muted:#8a8a8a;
  --light:#f4f5f7;
  --grey:#f0f0f0;
  --dark:#2b2b2b;
  --nav-active:#262626;
  --accent-red:#c0334d;
}
*{box-sizing:border-box;margin:0;padding:0}
html,body{width:1200px;height:3237px;overflow:hidden}
body{font-family:"Arimo",Arial,sans-serif;color:var(--ink);background:#fff;position:relative}
.photo{position:absolute;display:block}
/* header */
.header{position:absolute;left:0;top:0;width:1200px;height:132px;background:#fff}
.brand{position:absolute;left:62px;top:42px;display:flex;align-items:center;gap:12px}
.brand-mark{width:34px;height:34px;background:var(--blue)}
.brand-name{font-family:"Magra",sans-serif;font-weight:700;font-size:22px;line-height:1.05;color:var(--blue);letter-spacing:1px}
.social-top{position:absolute;left:920px;top:14px;display:flex;gap:3px}
.diamond{width:22px;height:22px;background:#111;transform:rotate(45deg);margin:4px}
.lang{position:absolute;left:1070px;top:23px;font-size:12px;display:flex;align-items:center;gap:6px}
.flag{width:16px;height:11px;background:linear-gradient(#c8102e 0 33%,#fff 33% 66%,#012169 66%)}
/* nav */
.nav{position:absolute;left:0;top:132px;width:1200px;height:51px;background:var(--blue);display:flex;align-items:center}
.nav a{color:#fff;text-decoration:none;font-size:16px;height:51px;line-height:51px;padding:0 26px}
.nav a.active{background:var(--nav-active);margin-left:48px;padding:0 26px}
.nav .search{position:absolute;right:50px;top:15px}
/* hero */
.hero{position:absolute;left:0;top:183px;width:1200px;height:607px;background:linear-gradient(90deg,#edf0f3 0%,#dfe4ea 30%,#9aa6b4 55%,#4a5a70 78%,#2a3548 100%)}
.hero-copy{position:absolute;left:50px;top:135px;width:560px}
.hero-welcome{font-family:"Montserrat",sans-serif;font-size:47px;color:#2a2a2a;line-height:1}
.hero-title{font-family:"Montserrat",sans-serif;font-weight:700;font-size:42px;color:var(--blue);margin-top:10px;letter-spacing:1px}
.hero-text{font-family:"Montserrat",sans-serif;font-size:16.5px;line-height:25px;color:#222;margin-top:8px;width:540px}
.btn-outline{display:inline-block;margin-top:38px;border:2px solid #222;padding:10px 26px;font-size:15px;color:#222;font-family:"Montserrat",sans-serif}
/* services */
.services{position:absolute;left:0;top:790px;width:1200px;height:665px;background:var(--light)}
.services-head{position:absolute;left:78px;top:68px;font-family:"Magra",sans-serif;font-weight:400;font-size:32px;line-height:40px;color:#222}
.services-rule{position:absolute;left:378px;top:55px;width:4px;height:108px;background:var(--blue)}
.services-intro{position:absolute;left:422px;top:68px;width:720px;font-size:13.5px;line-height:22px;color:#444}
.card{position:absolute;width:552px;height:176px;background:#fff;border:1px solid #e6e6e6}
.card .photo{left:6px;top:18px;width:150px;height:140px;border:4px solid #fff;box-shadow:0 1px 4px rgba(0,0,0,.2)}
.card h3{position:absolute;left:200px;top:28px;font-family:"Magra",sans-serif;font-size:18px;font-weight:400;color:#222}
.card .bar{position:absolute;left:200px;top:60px;width:42px;height:4px;background:var(--teal)}
.card p{position:absolute;left:200px;top:78px;width:330px;font-size:13.5px;line-height:24px;color:var(--muted)}
/* process */
.process{position:absolute;left:0;top:1455px;width:1200px;height:532px;background:var(--blue-bright)}
.process h2{position:absolute;left:0;width:1200px;top:42px;text-align:center;font-family:"Magra",sans-serif;font-weight:400;font-size:36px;color:#fff;letter-spacing:1px}
.step{position:absolute;top:112px;width:288px}
.step .photo{position:relative;width:288px;height:153px}
.step .label{background:var(--teal);color:#fff;font-family:"Magra",sans-serif;font-size:20px;text-align:center;height:47px;line-height:47px}
.step p{color:#fff;font-size:15.5px;line-height:24px;margin-top:20px}
/* why */
.why{position:absolute;left:0;top:1987px;width:1200px;height:386px;background:var(--grey)}
.why h2{position:absolute;left:540px;top:52px;font-family:"Magra",sans-serif;font-weight:400;font-size:36px;color:#222;letter-spacing:.5px}
.why .copy{position:absolute;left:540px;top:120px;width:600px;font-size:15.5px;line-height:25px;color:#333}
.why .copy p+p{margin-top:24px}
/* who */
.who{position:absolute;left:65px;top:2440px;width:650px}
.who h2{font-family:"Magra",sans-serif;font-weight:400;font-size:30px;color:#222}
.who .rule{width:255px;height:2px;background:var(--accent-red);margin-top:6px}
.who .rule-grey{width:640px;height:1px;background:#ddd;margin-top:-1px}
.who p{font-size:15.5px;line-height:24px;color:#333;margin-top:14px}
.who ul{list-style:none;margin-top:18px}
.who li{font-size:15.5px;line-height:32px;color:#333;padding-left:18px;position:relative}
.who li:before{content:"";position:absolute;left:2px;top:13px;width:6px;height:6px;border-radius:50%;background:var(--accent-red)}
.news{position:absolute;left:768px;top:2420px;width:352px;height:428px;background:var(--blue);padding:22px 16px}
.news h2{font-family:"Magra",sans-serif;font-weight:400;font-size:30px;color:#fff}
.news-item{position:absolute;left:18px;width:320px;height:70px}
.news-item .photo{left:0;top:0;width:76px;height:64px}
.news-item .meta{position:absolute;left:92px;top:0;color:#fff;font-size:13px;line-height:17px;width:228px}
.news-item b{display:block;font-style:italic}
.more{position:absolute;right:20px;bottom:16px;background:#111;color:#fff;font-size:13px;font-weight:700;padding:6px 10px}
/* footer */
.footer{position:absolute;left:0;top:2920px;width:1200px;height:317px;background:var(--dark);color:#fff;text-align:center}
.footer .brand-foot{position:absolute;left:0;width:1200px;top:55px;display:flex;justify-content:center;align-items:center;gap:12px}
.footer .brand-foot .brand-mark{background:#fff}
.footer .brand-foot span{font-family:"Magra",sans-serif;font-weight:700;font-size:22px;letter-spacing:1px}
.footer .links{position:absolute;left:0;width:1200px;top:150px;font-size:16px;letter-spacing:.5px}
.footer .copy{position:absolute;left:0;width:1200px;top:180px;font-size:15px}
.social-foot{position:absolute;left:484px;top:248px;display:flex;gap:12px}
.social-foot .diamond{background:#fff;width:26px;height:26px}
</style>
</head>
<body>

<header class="header">
  <div class="brand"><div class="brand-mark"></div><div class="brand-name">CALLOWAY<br>HOLDINGS</div></div>
  <div class="social-top"><div class="diamond"></div><div class="diamond"></div><div class="diamond"></div><div class="diamond"></div></div>
  <div class="lang"><span class="flag"></span>English</div>
</header>

<nav class="nav">
  <a class="active">Home</a><a>Services</a><a>Investment Approach</a><a>Missions and Values</a><a>Contact</a>
  <svg class="search" width="22" height="22" viewBox="0 0 22 22"><circle cx="9" cy="9" r="6.5" fill="none" stroke="#fff" stroke-width="2.5"/><line x1="14" y1="14" x2="20" y2="20" stroke="#fff" stroke-width="3"/></svg>
</nav>

<section class="hero" role="img" aria-label="Two businessmen in suits reviewing documents at a desk">
  <div class="hero-copy">
    <div class="hero-welcome">Welcome</div>
    <div class="hero-title">CALLOWAY HOLDINGS</div>
    <p class="hero-text">Vantra Is One Of The Leading Systems Integrators To The World's Finance Sector. We Are An Extension Of Your Business And Our Services Portfolio Has Been Built So You Always Have Access To A Complete Partner.</p>
    <span class="btn-outline">READ MORE</span>
  </div>
</section>

<section class="services">
  <h2 class="services-head">We offer<br>Different Services</h2>
  <div class="services-rule"></div>
  <p class="services-intro">Duis aute irure dolor in reprehenderit in voluptate velit esse cillum dolore eu fugiat nulla pariatur. Excepteur sint occaecat cupidatat non proident, sunt in culpa qui officia deserunt mollit anim id est laborum. Consect petur adipiscing elit.</p>

  <div class="card" style="left:48px;top:232px">
    <div class="photo" role="img" aria-label="Young couple smiling together" style="background:linear-gradient(135deg,#d8b8a0,#a0604e)"></div>
    <h3>Emploayee</h3><div class="bar"></div>
    <p>Neque porro quisquam est, qui dolorem ipsum quia dolor sit amet, consectetur, adipis civelit sed quia non numquam eius modi.</p>
  </div>
  <div class="card" style="left:624px;top:232px">
    <div class="photo" role="img" aria-label="Calculator and pen on financial papers" style="background:linear-gradient(135deg,#f0f0f0,#7a7a7a)"></div>
    <h3>IT Manager/CTO</h3><div class="bar"></div>
    <p>Neque porro quisquam est, qui dolorem ipsum quia dolor sit amet, consectetur, adipis civelit sed quia non numquam eius modi.</p>
  </div>
  <div class="card" style="left:48px;top:440px">
    <div class="photo" role="img" aria-label="Smiling businessman in a blue shirt" style="background:linear-gradient(135deg,#cfdcea,#5a7ea8)"></div>
    <h3>CFO</h3><div class="bar"></div>
    <p>Neque porro quisquam est, qui dolorem ipsum quia dolor sit amet, consectetur, adipis civelit sed quia non numquam eius modi.</p>
  </div>
  <div class="card" style="left:624px;top:440px">
    <div class="photo" role="img" aria-label="Thoughtful businessman at his desk" style="background:linear-gradient(135deg,#e4e0d8,#8a8276)"></div>
    <h3>Senior Hedge Fund Manager/CEO</h3><div class="bar"></div>
    <p>Neque porro quisquam est, qui dolorem ipsum quia dolor sit amet, consectetur, adipis civelit sed quia non numquam eius modi.</p>
  </div>
</section>

<section class="process">
  <h2>OUR PROCESS</h2>
  <div class="step" style="left:105px">
    <div class="photo" role="img" aria-label="Laptop on a wooden desk" style="background:linear-gradient(135deg,#3a2a20,#8a6a4a)"></div>
    <div class="label">ANALYSIS &amp; ASSESSMENT</div>
    <p>Our mission is to become a recognized Business Intelligence leader, delivering innovative solutions and professional services to established and emerging corporations.</p>
  </div>
  <div class="step" style="left:450px">
    <div class="photo" role="img" aria-label="Workspace with keyboard and colourful papers" style="background:linear-gradient(135deg,#e8e4dc,#c08a5a)"></div>
    <div class="label">IMPLEMENTATION</div>
    <p>We aspire to be a trusted advisor to our clients by providing them with tools and expertise to help them overcome challenges, enabling them to make informed business decisions.</p>
  </div>
  <div class="step" style="left:796px">
    <div class="photo" role="img" aria-label="Person working on a laptop" style="background:linear-gradient(135deg,#2a2a2a,#7a6a5a)"></div>
    <div class="label">ADAPT AND GROW</div>
    <p>Our mission is to become a recognized Business Intelligence leader, delivering innovative solutions and professional services to established and emerging corporations.</p>
  </div>
</section>

<section class="why">
  <div class="photo" role="img" aria-label="Tablet displaying website pages" style="left:100px;top:30px;width:380px;height:320px;background:linear-gradient(160deg,#f0f0f0,#c8ccd2 60%,#f0f0f0)"></div>
  <h2>Why Calloway Holdings</h2>
  <div class="copy">
    <p>Smaller boutique-style companies typically deliver more tailored solutions, aimed at resolving specific client problems. We put all of our energy into listening and understanding your needs, developing your custom solution, and striving to deliver above and beyond your requirements.</p>
    <p>We take pride in our work and treat your business initiatives as if they were ours, realizing that your success translates into ours.</p>
  </div>
</section>

<section class="who">
  <h2>Who Are We?</h2>
  <div class="rule"></div><div class="rule-grey"></div>
  <p>Meridel Software is a leading provider of data warehouse and business intelligence solutions. We help our customers create vision and define a technology strategy aligned to maximize operational efficiencies. We are an adept group of analysts, designers, programmers, and general business and technology enthusiasts that share a common goal of helping our customers succeed.</p>
  <p style="margin-top:24px">Our diverse expertise allows us to approach business challenges from a unique perspective, as we never let technology limitations restrict our ability to solve a problem.</p>
  <ul>
    <li>BI Program Development &amp; Assessment</li>
    <li>Data Warehouse Design</li>
    <li>Data Management Strategy</li>
    <li>Data Governance Development</li>
  </ul>
</section>

<aside class="news">
  <h2>Latest News</h2>
  <div class="news-item" style="top:92px">
    <div class="photo" role="img" aria-label="Business team meeting" style="background:linear-gradient(135deg,#e0e0e0,#707070)"></div>
    <div class="meta"><b>11/7/2013</b>Harvest the value from your existing implementation and let us transform your require.</div>
  </div>
  <div class="news-item" style="top:192px">
    <div class="photo" role="img" aria-label="Business team meeting" style="background:linear-gradient(135deg,#e0e0e0,#707070)"></div>
    <div class="meta"><b>11/7/2013</b>Harvest the value from your existing implementation and let us transform your require.</div>
  </div>
  <div class="news-item" style="top:292px">
    <div class="photo" role="img" aria-label="Business team meeting" style="background:linear-gradient(135deg,#e0e0e0,#707070)"></div>
    <div class="meta"><b>11/7/2013</b>Harvest the value from your existing implementation and let us transform your require.</div>
  </div>
  <span class="more">More Details &#8594;</span>
</aside>

<footer class="footer">
  <div class="brand-foot"><div class="brand-mark"></div><span>CALLOWAY HOLDINGS</span></div>
  <div class="links">HOME • SOLUTIONS • SERVICES • COMPANY • CONTACT</div>
  <div class="copy">Copyright © 2007 - 2015 calloway holdings, Inc. All Rights Reserved</div>
  <div class="social-foot"><div class="diamond"></div><div class="diamond"></div><div class="diamond"></div><div class="diamond"></div></div>
</footer>

</body>
</html>
```